Heronby Mortgage Capital Business Card

We need a business card design for our mortgage servicing company. In addition to servicing the loans of homeowners, we help homeowners with purchasing their homes and any mortgage refinancing. We would like to see designs that use the colors in the logo attached below (gold-ish yellow and navy blue), and any other design you deem fit! The design should communicate a simpler life with smart mortgages provided by Heronby.

```html
<!DOCTYPE html>
<html lang="en">
<head>
<meta charset="UTF-8">
<title>Heronby Mortgage Capital – Business Card</title>
<link href="https://fonts.googleapis.com/css2?family=Lato:wght@400;700;900&display=swap" rel="stylesheet">
<style>
  :root {
    --navy: #28225a;
    --gold: #e2ae35;
    --white: #ffffff;
    --ink: #1d1a33;
    --backdrop: #222222;
    --divider: #6b6488;
  }
  * { box-sizing: border-box; margin: 0; padding: 0; }
  html, body {
    width: 1200px; height: 1015px; overflow: hidden;
    background: var(--backdrop);
    font-family: 'Lato', sans-serif;
  }
  .canvas { position: relative; width: 1200px; height: 1015px; }
  .card {
    position: absolute; width: 560px; height: 320px;
    box-shadow: 0 10px 30px rgba(0,0,0,.55);
    overflow: hidden;
  }
  .card-back { left: 110px; top: 110px; background: var(--navy); }
  .card-front { left: 530px; top: 570px; background: var(--white); }

  .wordmark {
    position: absolute; left: 0; right: 0; text-align: center;
    color: var(--gold); font-weight: 900; font-size: 44px; letter-spacing: 1px;
  }
  .card-back .wordmark { top: 128px; }
  .card-front .wordmark { top: 62px; }

  .info-band {
    position: absolute; left: 0; right: 0; top: 172px; height: 102px;
    background: var(--navy); display: flex; align-items: center;
  }
  .person { width: 300px; text-align: right; padding-right: 18px; }
  .person-name { color: var(--gold); font-weight: 900; font-size: 21px; letter-spacing: .5px; }
  .person-title { color: var(--white); font-size: 15px; margin-top: 2px; }
  .band-divider { width: 1px; height: 62px; background: var(--divider); }
  .contacts { list-style: none; padding-left: 18px; }
  .contacts li {
    display: flex; align-items: center; gap: 9px;
    color: var(--white); font-size: 14px; line-height: 22px;
  }
  .contacts svg { width: 14px; height: 14px; fill: var(--gold); flex: none; }
  .address {
    position: absolute; left: 0; right: 0; bottom: 14px; text-align: center;
    color: var(--ink); font-size: 15px;
  }
</style>
</head>
<body>
<main class="canvas">
  <section class="card card-back" aria-label="Card back">
    <div class="wordmark">Heronby Mortgage</div>
  </section>

  <section class="card card-front" aria-label="Card front">
    <div class="wordmark">Heronby Mortgage</div>
    <div class="info-band">
      <div class="person">
        <div class="person-name">DANIEL ARCHER</div>
        <div class="person-title">Managing Director</div>
      </div>
      <div class="band-divider"></div>
      <ul class="contacts">
        <li>
          <svg viewBox="0 0 24 24" aria-hidden="true"><path d="M6.6 10.8a15.1 15.1 0 0 0 6.6 6.6l2.2-2.2a1 1 0 0 1 1-.25 11.4 11.4 0 0 0 3.6.57 1 1 0 0 1 1 1V20a1 1 0 0 1-1 1A17 17 0 0 1 3 4a1 1 0 0 1 1-1h3.5a1 1 0 0 1 1 1c0 1.25.2 2.45.57 3.57a1 1 0 0 1-.25 1z"/></svg>
          044-987 654 321
        </li>
        <li>
          <svg viewBox="0 0 24 24" aria-hidden="true"><path d="M2 5h20v14H2z M2 5l10 8 10-8" fill="none" stroke="#e2ae35" stroke-width="2"/><path d="M2 5h20l-10 8z"/></svg>
          hello@heronbyhome.com
        </li>
        <li>
          <svg viewBox="0 0 24 24" aria-hidden="true"><circle cx="12" cy="12" r="9.5" fill="none" stroke="#e2ae35" stroke-width="2"/><path d="M2.5 12h19M12 2.5c3 3 3 16 0 19M12 2.5c-3 3-3 16 0 19" fill="none" stroke="#e2ae35" stroke-width="1.6"/></svg>
          www.heronbyhome.com
        </li>
      </ul>
    </div>
    <div class="address">87, Harbor Lane here, Westfield City, 30218</div>
  </section>
</main>
</body>
</html>
```